Steelcrest Process Systems. Needs a Business Card Design

We need a business card design for an engineering company which supplies industrial components (pumps, compressors, mechanical seals) provides repairs and services for above mentioned equipments. We offer a uniqe engineering solutions which help our customers to increase the productivness of their manufacturings, and energy savings.

Target Market(s)

Chemical and energy plants, refineries. Food industry and private consumers in a less.

Industry/Entity Type

Business

Contact Information for Business Card

Stylish and sleek design oriented on industrial area.

Requirements
Should not have
• company name shortening

```html
<!DOCTYPE html>
<html lang="uk">
<head>
<meta charset="utf-8">
<title>Steelcrest Process Systems — Business Card</title>
<link rel="stylesheet" href="https://fonts.googleapis.com/css2?family=Ubuntu:wght@500&family=Open+Sans:ital,wght@0,400;1,600&family=Questrial&display=swap">
<style>
  :root {
    --page: #e7e1d3;
    --card-dark: #12161d;
    --card-mid: #1c222c;
    --card-back-mid: #232a37;
    --steel: #5a6474;
    --steel-light: #9aa4b2;
    --text: #ffffff;
    --text-soft: #e6e8ec;
    --accent: #e2261d;
  }
  * { margin: 0; padding: 0; box-sizing: border-box; }
  html, body { width: 1200px; height: 1155px; overflow: hidden; }
  body { background: var(--page); position: relative; }

  .card {
    position: absolute;
    left: 275px;
    width: 650px;
    overflow: hidden;
    color: var(--text);
  }
  .card--front {
    top: 165px; height: 380px;
    background: radial-gradient(ellipse at 70% 30%, var(--card-mid) 0%, var(--card-dark) 75%);
  }
  .card--back {
    top: 578px; height: 384px;
    background: radial-gradient(ellipse at 45% 55%, var(--card-back-mid) 0%, var(--card-dark) 80%);
  }

  .brand-dot {
    position: absolute;
    border-radius: 50%;
    background: var(--accent);
  }
  .card--front .brand-dot { left: 52px; top: 58px; width: 62px; height: 62px; }
  .card--back .brand-dot { left: 50px; top: 70px; width: 62px; height: 62px; }

  .company-name {
    position: absolute;
    left: 138px; top: 66px;
    font-family: "Ubuntu", sans-serif;
    font-weight: 500;
    font-size: 34px;
    letter-spacing: 0.2px;
    color: var(--text);
    white-space: nowrap;
  }

  .contact-list {
    position: absolute;
    left: 268px; top: 148px;
    list-style: none;
    font-family: "Open Sans", sans-serif;
    font-size: 21px;
    color: var(--text-soft);
  }
  .contact-list li { display: flex; align-items: center; height: 30px; }
  .contact-list svg { width: 20px; height: 20px; margin-right: 14px; flex: none; }

  .address {
    position: absolute;
    left: 268px; top: 257px;
    font-family: "Open Sans", sans-serif;
    font-style: italic;
    font-weight: 600;
    font-size: 18px;
    line-height: 28px;
    color: var(--text-soft);
  }

  .gear-corner { position: absolute; left: 0; top: 0; width: 650px; height: 380px; }

  .tech-backdrop { position: absolute; left: 0; top: 0; width: 650px; height: 384px; }

  .person-name {
    position: absolute;
    left: 182px; top: 72px;
    font-family: "Questrial", sans-serif;
    font-size: 40px;
    color: var(--text);
  }
  .person-title {
    position: absolute;
    left: 188px; top: 123px;
    font-family: "Questrial", sans-serif;
    font-size: 20px;
    letter-spacing: 0.5px;
    color: var(--text-soft);
  }
  .direct-contacts {
    position: absolute;
    left: 330px; top: 262px;
    list-style: none;
    font-family: "Questrial", sans-serif;
    color: var(--text-soft);
  }
  .direct-contacts li { display: flex; align-items: center; }
  .direct-contacts .phone { font-size: 28px; height: 40px; color: var(--text); }
  .direct-contacts .email { font-size: 22px; height: 36px; }
  .direct-contacts svg { width: 22px; height: 22px; margin-right: 20px; flex: none; }
</style>
</head>
<body>

<section class="card card--front" aria-label="Card front">
  <svg class="gear-corner" viewBox="0 0 650 380" aria-hidden="false">
    <defs>
      <linearGradient id="gearFill" x1="0" y1="0" x2="1" y2="1">
        <stop offset="0" stop-color="#2a313c"/>
        <stop offset="0.55" stop-color="#6c7482"/>
        <stop offset="1" stop-color="#20262f"/>
      </linearGradient>
    </defs>
    <polygon role="img" aria-label="Illustration of interlocking machine gears" points="0,194 0,380 254,380" fill="url(#gearFill)"/>
    <line x1="0" y1="194" x2="254" y2="380" stroke="#f2f2f2" stroke-width="2"/>
  </svg>

  <span class="brand-dot" aria-hidden="true"></span>
  <h1 class="company-name">Steelcrest Process Systems</h1>

  <ul class="contact-list">
    <li>
      <svg viewBox="0 0 20 20"><circle cx="10" cy="10" r="8.5" fill="none" stroke="var(--accent)" stroke-width="1.8"/><path d="M6.5 6.2c0 4 3.3 7.3 7.3 7.3l.7-1.8-2-1-1 1a5 5 0 0 1-3-3l1-1-1-2z" fill="var(--accent)"/></svg>
      044 301 27 19
    </li>
    <li>
      <svg viewBox="0 0 20 20"><rect x="5" y="2" width="10" height="6" fill="var(--accent)"/><rect x="2" y="8" width="16" height="10" rx="1.5" fill="var(--accent)"/><rect x="5" y="11" width="7" height="2" fill="#12161d"/><rect x="5" y="14" width="7" height="2" fill="#12161d"/></svg>
      044 301 27 20
    </li>
    <li>
      <svg viewBox="0 0 20 20" fill="none" stroke="var(--accent)" stroke-width="1.6"><circle cx="10" cy="10" r="8.5"/><ellipse cx="10" cy="10" rx="3.8" ry="8.5"/><line x1="1.5" y1="10" x2="18.5" y2="10"/><line x1="3" y1="5.5" x2="17" y2="5.5"/><line x1="3" y1="14.5" x2="17" y2="14.5"/></svg>
      STEELCREST.EXAMPLE
    </li>
  </ul>

  <p class="address">пр. Заводской, д. 24 а,<br>Днiпро, Украина, 49000</p>
</section>

<section class="card card--back" aria-label="Card back">
  <svg class="tech-backdrop" viewBox="0 0 650 384">
    <defs>
      <radialGradient id="techGlow" cx="0.5" cy="0.5" r="0.5">
        <stop offset="0" stop-color="#3a4452" stop-opacity="0.55"/>
        <stop offset="1" stop-color="#1a2029" stop-opacity="0"/>
      </radialGradient>
    </defs>
    <ellipse role="img" aria-label="Faint backdrop of gears and technical dial shapes" cx="260" cy="230" rx="300" ry="170" fill="url(#techGlow)"/>
  </svg>

  <span class="brand-dot" aria-hidden="true"></span>
  <h2 class="person-name">Your Name</h2>
  <p class="person-title">YOUR TITLE</p>

  <ul class="direct-contacts">
    <li class="phone">
      <svg viewBox="0 0 20 20"><circle cx="10" cy="10" r="8.5" fill="none" stroke="var(--accent)" stroke-width="1.8"/><path d="M6.5 6.2c0 4 3.3 7.3 7.3 7.3l.7-1.8-2-1-1 1a5 5 0 0 1-3-3l1-1-1-2z" fill="var(--accent)"/></svg>
      044 301 27 19
    </li>
    <li class="email">
      <svg viewBox="0 0 22 16" fill="none" stroke="var(--accent)" stroke-width="1.8"><rect x="1" y="1" width="20" height="14"/><polyline points="1,1 11,9 21,1"/></svg>
      email@website.com
    </li>
  </ul>
</section>

</body>
</html>
```